External Shop Front Signage Design

We need design ideas for outdoor signage to go on our shopfront, windows and glass doors at our new location for Kestrel Physio. We want to use our existing logo and colour schemes but want it to be dark/black background to match our new gym facility & so that the colours & writing stand out from the street. We would like it to be a minimalist, modern design but also be clear that we are a physiotherapy practice with a gym facility. We have tried some designs but have found them to be too busy, and too many words. We would like something more classy, clear, and simple. I have attached photos of the current street views & some of the designs we have had put together that we didn't like. Our logo is attached as well and our website for reference is www.kestrelclinic.com.au

Industry/Entity Type

Physiotherapy / Health

Font styles to use
Other font styles liked:
• Lufga Bold or Poppins Bold/Itallic

Colors
00AB8E
00BBA5
67D7C9
C6EFE9
E9F9F6
59FF00
82FF00
B8FF75
E3FFCB
F4FFEA

Requirements
Must have
• Obvious logo that pops when driving past
Nice to have
• Something that makes it clear we are mainly physiotherapy with gym facility
Should not have
• Too many words

```html
<!DOCTYPE html>
<html lang="en">
<head>
<meta charset="utf-8">
<title>Kestrel Physio – Street Left Signage</title>
<link href="https://fonts.googleapis.com/css2?family=Poppins:ital,wght@0,500;0,600;0,700;1,800&display=swap" rel="stylesheet">
<style>
  :root {
    --canvas: #eeeae5;
    --sign-black: #000000;
    --text-white: #ffffff;
    --label-red: #d9232a;
    --frame-tan: #bf8a6b;
    --frame-green: #234a42;
    --lime: #b8ff00;
    --green: #82f04a;
    --mint: #58eb93;
    --teal: #3ee8cc;
    --accent-gradient: linear-gradient(90deg, var(--lime) 0%, var(--green) 45%, var(--mint) 70%, var(--teal) 100%);
  }
  * { margin: 0; padding: 0; box-sizing: border-box; }
  html, body { width: 1200px; height: 921px; overflow: hidden; }
  body {
    position: relative;
    background: var(--canvas);
    font-family: "Poppins", Arial, sans-serif;
  }
  .view-label {
    position: absolute; top: 14px; left: 0; width: 1200px;
    text-align: center; color: var(--label-red);
    font-weight: 700; font-size: 42px; letter-spacing: 1px; line-height: 1;
  }
  .fascia {
    position: absolute; left: 159px; top: 124px; width: 957px; height: 177px;
    background: var(--sign-black);
  }
  .fascia::after {
    content: ""; position: absolute; left: 0; bottom: 0; width: 100%; height: 8px;
    background: var(--accent-gradient);
  }
  .wordmark {
    position: absolute; color: var(--text-white);
    font-weight: 600; line-height: 1; letter-spacing: -2px;
  }
  .fascia .wordmark { left: 0; width: 100%; top: 28px; text-align: center; font-size: 104px; }

  .window-panel {
    position: absolute; left: 334px; top: 372px; width: 611px; height: 364px;
    background: var(--frame-tan);
  }
  .tagline-box {
    position: absolute; left: 21px; top: 12px; width: 573px; height: 75px;
    background: var(--sign-black);
    display: flex; align-items: center; justify-content: center;
  }
  .tagline {
    font-weight: 800; font-style: italic; font-size: 25.5px; letter-spacing: -0.3px;
    background: var(--accent-gradient); -webkit-background-clip: text; background-clip: text;
    color: transparent;
  }
  .pane-frame {
    position: absolute; left: 21px; top: 98px; width: 573px; height: 247px;
    background: var(--frame-green);
  }
  .pane {
    position: absolute; top: 4px; height: 235px; background: var(--sign-black);
  }
  .pane::after {
    content: ""; position: absolute; left: 0; bottom: 0; width: 100%; height: 6px;
  }
  .pane-services { left: 4px; width: 235px; }
  .pane-services::after { background: linear-gradient(90deg, var(--lime), var(--green)); }
  .pane-centre { left: 248px; width: 155px; }
  .pane-centre::after { background: linear-gradient(90deg, var(--green), var(--mint)); }
  .pane-access { left: 412px; width: 157px; }
  .pane-access::after { background: linear-gradient(90deg, var(--mint), var(--teal)); }

  .service-list {
    list-style: none; position: absolute; left: 16px; top: 16px;
    color: var(--text-white); font-weight: 700; font-size: 13.5px; line-height: 34.2px;
  }
  .access-note {
    position: absolute; left: 18px; bottom: 20px; width: 130px;
    color: var(--text-white); font-weight: 500; font-size: 10.5px; line-height: 14px; letter-spacing: 0.3px;
  }
  .window-panel .wordmark { left: 278px; top: 162px; font-size: 86px; }
</style>
</head>
<body>
  <h1 class="view-label">STREET LEFT</h1>

  <section class="fascia" aria-label="Fascia sign">
    <div class="wordmark">kestrel</div>
  </section>

  <section class="window-panel" aria-label="Window signage">
    <div class="tagline-box">
      <p class="tagline">GET BETTER. GET MOVING. GET STRONG.</p>
    </div>
    <div class="pane-frame">
      <div class="pane pane-services">
        <ul class="service-list">
          <li>PHYSIOTHERAPY</li>
          <li>REMEDIAL MASSAGE</li>
          <li>PODIATRY</li>
          <li>HYDROTHERAPY</li>
          <li>ATHLETIC DEVELOPMENT</li>
          <li>STRENGHT&amp;CONDITIONING</li>
        </ul>
      </div>
      <div class="pane pane-centre"></div>
      <div class="pane pane-access">
        <p class="access-note">ENTRANCE &amp; PARKING<br>AT REAR OF BUILDING</p>
      </div>
    </div>
    <div class="wordmark">kestrel</div>
  </section>
</body>
</html>
```